Willowmere Pet Farewells - business cards & brand stationary

We already have a logo and the colors and a website. Need a business card designed that will be able to customized to multiple veterinarians who will be partnering with us. The feel needs to be compassionate, comforting with our tagline 'A Gift of Love at Home'. It will be 2 sides.
On the back our platform/partner vets will be customizing each business card with their own service areas, phone numbers, name and title. On the front, i would like to see experimentation with use of our photos, the logo, tagline and a description 'Peaceful and Compassionate At-Home Pet Euthanasia'

```html
<!DOCTYPE html>
<html lang="en">
<head>
<meta charset="utf-8">
<title>Willowmere Pet Farewells – Business Cards</title>
<link href="https://fonts.googleapis.com/css2?family=Raleway:wght@300;400;700;800&display=swap" rel="stylesheet">
<style>
  :root {
    --stage: #d8d8d8;
    --navy: #1c2840;
    --photo-dark: #101726;
    --photo-mid: #2c3550;
    --brand-blue: #79a0cc;
    --soft-blue: #e1e7f1;
    --paler-blue: #f1f4f9;
    --paper: #ffffff;
  }
  * { box-sizing: border-box; margin: 0; padding: 0; }
  html, body {
    width: 1200px; height: 846px; overflow: hidden;
    background: var(--stage);
    font-family: "Raleway", sans-serif;
  }
  .stationery {
    position: relative; width: 1200px; height: 846px;
    display: flex; align-items: center; justify-content: center; gap: 48px;
  }
  .card {
    position: relative; width: 520px; height: 370px; overflow: hidden;
    box-shadow: 0 14px 30px rgba(0,0,0,0.18);
  }

  /* Front */
  .card-front { background: var(--navy); }
  .card-front .photo {
    position: absolute; top: 0; right: 0; width: 300px; height: 200px;
    background: radial-gradient(ellipse at 55% 45%, var(--photo-mid) 0%, var(--photo-dark) 60%, var(--navy) 100%);
    border-bottom-left-radius: 60% 40%;
  }
  .card-front .brand {
    position: absolute; left: 44px; top: 212px; color: var(--brand-blue);
  }
  .brand-name {
    display: flex; align-items: center; gap: 14px;
    font-size: 40px; font-weight: 700; letter-spacing: 0.5px; line-height: 1;
  }
  .brand-dot {
    width: 38px; height: 38px; border-radius: 50%; background: var(--brand-blue);
  }
  .tagline {
    margin-top: 10px; margin-left: 52px;
    font-size: 15px; font-weight: 300;
  }
  .description {
    margin-top: 16px; margin-left: 52px;
    font-size: 17px; font-weight: 300; line-height: 1.3;
  }

  /* Back */
  .card-back { background: var(--paper); }
  .card-back .wash { position: absolute; inset: 0; }
  .card-back .brand-name {
    position: absolute; left: 40px; top: 84px;
    color: var(--brand-blue); font-size: 30px;
  }
  .card-back .brand-dot { width: 30px; height: 30px; }
  .contact { position: absolute; left: 40px; top: 160px; color: var(--brand-blue); }
  .person-name { font-size: 24px; font-weight: 800; }
  .person-title { font-size: 19px; font-weight: 300; margin-top: 2px; }
  .contact-list { list-style: none; margin-top: 18px; }
  .contact-list li {
    display: flex; align-items: center; gap: 8px;
    font-size: 18px; font-weight: 300; line-height: 1.4;
  }
  .contact-list svg { width: 20px; height: 20px; flex: none; }
</style>
</head>
<body>
<main class="stationery">

  <section class="card card-front">
    <div class="photo" role="img" aria-label="Photograph of an elderly black dog with a greying muzzle, looking to the side"></div>
    <div class="brand">
      <div class="brand-name"><span class="brand-dot"></span>Willowmere</div>
      <p class="tagline">A gift of love at home.</p>
      <p class="description">Peaceful and Compassionate<br>At-Home Pet Euthanasia</p>
    </div>
  </section>

  <section class="card card-back">
    <svg class="wash" viewBox="0 0 520 370" aria-hidden="true">
      <path d="M150 0 Q260 190 520 210 L520 0 Z" fill="var(--paler-blue)"/>
      <path d="M265 0 Q290 150 520 160 L520 0 Z" fill="var(--soft-blue)"/>
    </svg>
    <div class="brand-name"><span class="brand-dot"></span>Willowmere</div>
    <div class="contact">
      <p class="person-name">Name Lastname</p>
      <p class="person-title">Title</p>
      <ul class="contact-list">
        <li>
          <svg viewBox="0 0 20 20" aria-hidden="true"><circle cx="10" cy="10" r="10" fill="var(--brand-blue)"/><path d="M7 5.5l1.6 2.4-1 1c.6 1.3 1.6 2.3 2.9 2.9l1-1 2.4 1.6-.8 1.6c-3.6-.4-6.3-3.1-6.7-6.7z" fill="#fff"/></svg>
          (555) 010-2468
        </li>
        <li>
          <svg viewBox="0 0 20 20" aria-hidden="true"><circle cx="10" cy="10" r="10" fill="var(--brand-blue)"/><rect x="5" y="6.5" width="10" height="7" fill="#fff"/><path d="M5 6.5l5 4 5-4" fill="none" stroke="var(--brand-blue)" stroke-width="1"/></svg>
          contact@willowmerepets.com
        </li>
        <li>
          <svg viewBox="0 0 20 20" aria-hidden="true"><circle cx="10" cy="10" r="10" fill="var(--brand-blue)"/><path d="M10 4.5a3.5 3.5 0 0 0-3.5 3.5c0 2.6 3.5 7 3.5 7s3.5-4.4 3.5-7A3.5 3.5 0 0 0 10 4.5z" fill="#fff"/><circle cx="10" cy="8" r="1.3" fill="var(--brand-blue)"/></svg>
          Service areas: Your Region Here
        </li>
      </ul>
    </div>
  </section>

</main>
</body>
</html>
```